Buch-Cover für Romantik-Drama gesucht
Zielgruppe
Autorin
Belletristik
Hallo,
ich suche für meinen Roman ein passendes Cover.
Die Handlung des Romans mit dem Titel „Stille Wehmutstage“ ist als Romantik–Drama zu bezeichnen.
Für einen kleinen Einblick in den Text habe ich ein paar Textstellen beigefügt.
In der Handlung geht es um eine junge Pianistin.
Von ihrem musikalischen Partner körperlich misshandelt, verliert sie ihr gemeinsames Kind.
Nach ihrer Rückkehr nach Deutschland legt sie sich selber den Verzicht auf das geliebte Klavier und die Musik als Buße auf. Durch ihre Freunde und ein ungewöhnliches Angebot findet sie einen Weg zurück zur Musik und endlich die Liebe.
Ich möchte kein triviales Kitsch– Cover
Ein kleiner Wiedererkennungseffekt zum beigefügten Cover – einem eigenständigen Roman, der jedoch in einer losen Verbindung zu „Stille Wehmutstage“ steht, wäre schön.
Ein passendes Tastatur/ Flügel–Bild kann ich bei Bedarf zur Verfügung stellen.
Viel Freude bei der Covergestaltung
Henrike Luise Talbach

```html
<!DOCTYPE html>
<html lang="de">
<head>
<meta charset="utf-8">
<title>Stille Wehmutstage – Umschlag</title>
<link rel="stylesheet" href="https://fonts.googleapis.com/css2?family=Cormorant+Garamond:wght@400;500;600&display=swap">
<style>
  :root {
    --page: #ffffff;
    --ink-black: #070707;
    --accent-orange: #e8801e;
    --blurb-text: #d9d9d9;
    --imprint-ink: #ffffff;
    --serif: "Cormorant Garamond", Georgia, serif;
  }
  html, body {
    margin: 0;
    padding: 0;
    width: 896px;
    height: 1200px;
    overflow: hidden;
    background: var(--page);
  }
  .cover-spread {
    position: absolute;
    left: 20px;
    top: 295px;
    width: 856px;
    height: 609px;
    font-family: var(--serif);
    overflow: hidden;
  }
  .photo-area {
    position: absolute;
    top: 0;
    left: 0;
    width: 856px;
    height: 609px;
  }
  .panel {
    position: absolute;
    top: 0;
    height: 609px;
  }
  .panel--back { left: 0; width: 402px; }
  .panel--spine { left: 402px; width: 40px; }
  .panel--front { left: 442px; width: 414px; }

  .author {
    position: absolute;
    top: 22px;
    left: 0;
    right: 0;
    margin: 0;
    text-align: center;
    color: var(--accent-orange);
    font-size: 22px;
    font-weight: 400;
    letter-spacing: 0.04em;
  }
  .title {
    position: absolute;
    left: 0;
    right: 0;
    margin: 0;
    text-align: center;
    color: var(--accent-orange);
    font-weight: 600;
    line-height: 0.95;
  }
  .title__line { display: block; }
  .panel--back .title { top: 88px; }
  .panel--back .title__line--small { font-size: 36px; }
  .panel--back .title__line--large { font-size: 50px; }
  .panel--front .title { top: 66px; }
  .panel--front .title__line--small { font-size: 40px; }
  .panel--front .title__line--large { font-size: 57px; }

  .blurb {
    position: absolute;
    top: 232px;
    left: 56px;
    width: 290px;
    margin: 0;
    text-align: center;
    color: var(--blurb-text);
    font-size: 10.5px;
    line-height: 13.6px;
  }
  .blurb p { margin: 0 0 13.6px; }

  .spine-text {
    position: absolute;
    top: 0;
    left: 40px;
    width: 609px;
    height: 40px;
    transform-origin: 0 0;
    transform: rotate(90deg);
    display: flex;
    align-items: center;
    white-space: nowrap;
  }
  .spine-text__imprint {
    margin-left: 22px;
    color: var(--imprint-ink);
    font-size: 12px;
  }
  .spine-text__author {
    margin-left: 80px;
    color: var(--accent-orange);
    font-size: 14px;
    letter-spacing: 0.04em;
  }
  .spine-text__title {
    margin-left: 26px;
    color: var(--accent-orange);
    font-size: 22px;
    font-weight: 600;
  }
  .imprint {
    position: absolute;
    left: 30px;
    bottom: 30px;
    margin: 0;
    color: var(--imprint-ink);
    font-size: 20px;
    font-weight: 400;
  }
</style>
</head>
<body>
  <section class="cover-spread">
    <svg class="photo-area" role="img" aria-label="Fotografie: Pianistin am Flügel im Gegenlicht, Flügel über Rückseite und Vorderseite gezogen" viewBox="0 0 856 609" width="856" height="609">
      <defs>
        <linearGradient id="back-tone" x1="0" y1="0" x2="1" y2="0">
          <stop offset="0" stop-color="#050505"/>
          <stop offset="0.45" stop-color="#1a1612"/>
          <stop offset="1" stop-color="#080808"/>
        </linearGradient>
        <linearGradient id="front-tone" x1="0" y1="0" x2="0.6" y2="1">
          <stop offset="0" stop-color="#ffffff"/>
          <stop offset="0.4" stop-color="#f4f1ed"/>
          <stop offset="0.7" stop-color="#3a332c"/>
          <stop offset="1" stop-color="#050505"/>
        </linearGradient>
      </defs>
      <rect x="0" y="0" width="442" height="609" fill="url(#back-tone)"/>
      <rect x="442" y="0" width="414" height="609" fill="url(#front-tone)"/>
    </svg>

    <div class="panel panel--back">
      <p class="author">H. L. TALBACH</p>
      <h2 class="title">
        <span class="title__line title__line--small">Stille</span>
        <span class="title__line title__line--large">Wehmutstage</span>
      </h2>
      <div class="blurb">
        <p>Freunde sind ein Geschenk.<br>Wenn alles aussichtslos erscheint, ist es gut, sie an deiner Seite zu wissen.</p>
        <p>Die junge Pianistin Clara versucht ihr Leben wieder in den Griff zu bekommen, seit sie aus Moskau zurück ist. Beruflich beschreitet sie neue Wege, obwohl sie damit ihre eigentliche Sehnsucht unterdrückt. Ihre mühsam aufgebaute Fassade fängt an zu bröckeln, als Alexander, ein Freund ihrer Schwester, sich in ihr Leben einmischt. Doch die Schatten der Vergangenheit ruhen nicht und Clara hat keine Chance ihnen zu entkommen.</p>
      </div>
    </div>

    <div class="panel panel--spine">
      <div class="spine-text">
        <span class="spine-text__imprint">Hallweg</span>
        <span class="spine-text__author">H. L. TALBACH</span>
        <span class="spine-text__title">Stille Wehmutstage</span>
      </div>
    </div>

    <div class="panel panel--front">
      <p class="author">H. L. TALBACH</p>
      <h1 class="title">
        <span class="title__line title__line--small">Stille</span>
        <span class="title__line title__line--large">Wehmutstage</span>
      </h1>
      <p class="imprint">Hallweg</p>
    </div>
  </section>
</body>
</html>
```